Harvest Velmora website and logo design

Looking to create a personal finance service website. My goal is for this website to be a resource repository where potential clients could come to get resources that they may find helpful for their personal use. I would like the website to have ways to collect emails from people who visit my website so I can send them periodic newsletters. I would like the website to have the following sections: A blog page, a resource page, a book review page (with potential affiliate links), An icon for a link to my podcast link ( titled Coin Climbers Working of getting this off the ground) ( I need a design for this podcast page as well) (coin climbers podcast is intended to interview everyday people who are on their journey to creating wealth, interview them and find out what is working for them) (design inspiration is an individual stacking a pile of gold) a section asking people to schedule a strategy coaching call, an about page.

I currently have a website with Word press titled Keliruston.com. The fron page should be about mira and a link to the harvest velmor platform. I would like to house harvest velmora on this site. I currently do not have a logo for harvest Velmora as well so I would like that or I can create a logo design request? The tag line should be Harvest Velmora… beside you. Helping your money grow branches.

The atmosphere I would like to have set for the site is that of calming colors that will put people at ease. The color green (vibrant green like that of a leaf) and gold is what I have in mind as my main color.
The vision of logo I have in mind to be incorporated through the website is that off a tree filled with money. The tree should have many roots and Money should be flowing through different channels of the roots. The goal is to teach people to give their money roots to go where they intend it to go rather than them wondering where their money went to every month.

The name of my business is harvest Velmora (pronounced: Velmoira). The idea is that harvest velmora with you. It does not escape you. So you are like a try planted and your money goes to where you intend them to go. You are intentional about your finance.

Target audience is men and women between the ages of 25-45. Core age is about 30 though. My targeted audience is the person who desires to have control over their finances by taking the appropriate action necessary. they are action oriented and go getters. They like to have resources at hand that will help them make informed decisions.
I would like images of real people looking at peace with the state of their well being.
Examples of websites I like are:
www.brightpursefolio.com/
https://www.tradelantern.com/
https://www.nadiquerovan.com/
https://velquist.tv/
https://maribelthorncrest.com/

Target Market(s)

Men and Women of all Race age 25-35

Logo Text

Harvest Velmora

Coding

Coded - Design and coding required

Number of Pages Required

4 page

Font styles to use
Serif
Decorative

Colors

Designer to choose colors to be used in the design.

```html
<!DOCTYPE html>
<html lang="en">
<head>
<meta charset="utf-8">
<title>Harvest Velmora</title>
<link rel="stylesheet" href="https://fonts.googleapis.com/css2?family=IBM+Plex+Sans:wght@400;600;700&family=Oswald:wght@400;500;600&family=Roboto:wght@400;500;700&family=Poppins:wght@400;500&display=swap">
<style>
:root{
  --green:#7cb82f;
  --green-dark:#5f9a1f;
  --orange:#d9820f;
  --ink:#222;
  --text:#555;
  --muted:#777;
  --gray:#ececec;
  --footer:#1e1e1e;
  --white:#fff;
}
*{margin:0;padding:0;box-sizing:border-box}
html,body{width:1200px;height:5034px;overflow:hidden}
body{position:relative;font-family:'Roboto',sans-serif;color:var(--text);background:var(--white)}
.abs{position:absolute}
.fill{position:absolute}
.section-title{position:absolute;left:0;width:1200px;text-align:center;font-family:'IBM Plex Sans',sans-serif;font-weight:700;font-size:37px;color:var(--ink);letter-spacing:1px}
.title-rule{position:absolute;left:562px;width:76px;height:4px;background:var(--green)}
.btn{position:absolute;display:flex;align-items:center;justify-content:center;font-family:'Roboto',sans-serif;font-weight:500;color:var(--white);letter-spacing:.5px;text-transform:uppercase}

/* header / hero */
.hero{left:0;top:0;width:1200px;height:745px;background:linear-gradient(110deg,#cfd3d6 0%,#e7e4df 35%,#f1efec 60%,#d8dde0 100%)}
.brand{left:120px;top:14px;display:flex;flex-direction:column;align-items:center}
.brand-dot{width:62px;height:62px;border-radius:50%;background:var(--green)}
.brand-name{margin-top:10px;font-family:'Oswald',sans-serif;font-weight:600;font-size:22px;color:var(--ink);letter-spacing:.3px;text-transform:uppercase}
.call{left:714px;top:28px;display:flex;align-items:center;gap:10px;font-family:'Oswald',sans-serif;font-size:17px;color:var(--ink)}
.register{left:960px;top:25px;width:96px;height:37px;background:var(--orange);font-family:'Oswald',sans-serif;font-size:14px}
.nav{left:580px;top:84px;display:flex;gap:22px;font-family:'Oswald',sans-serif;font-size:16px;color:var(--ink);text-transform:uppercase}
.nav .active{color:var(--green)}
.hero-box{left:613px;top:232px;width:443px;height:238px;background:rgba(40,40,40,.82);padding:18px 34px}
.hero-box h1{font-family:'Oswald',sans-serif;font-weight:600;font-size:38px;line-height:41px;color:var(--white)}
.hero-btn{left:647px;top:398px;width:168px;height:45px;background:var(--orange);font-size:15px}
.dots{left:573px;top:710px;display:flex;gap:4px}
.dots span{width:14px;height:14px;border-radius:50%;border:2px solid #333;background:transparent}
.dots span.on{background:#333}

/* services */
.service{top:928px;width:280px;height:352px;border:2px solid #ddd;text-align:center;padding:30px 24px 0}
.service-icon{width:106px;height:106px;border-radius:50%;background:var(--green);margin:0 auto;display:flex;align-items:center;justify-content:center}
.service h3{margin-top:30px;font-family:'Roboto',sans-serif;font-weight:700;font-size:15px;color:var(--ink);letter-spacing:.5px}
.service p{margin-top:12px;font-size:13.5px;line-height:22px;color:var(--text)}

/* welcome */
.welcome-art{left:0;top:1386px;width:596px;height:484px;background:radial-gradient(circle at 30% 20%,#e7f0a6 0%,#7fa53c 35%,#3b4a1f 75%,#2a2416 100%)}
.welcome{left:596px;top:1386px;width:604px;height:484px;background:var(--orange);padding:70px 64px 0}
.welcome h4{font-family:'IBM Plex Sans',sans-serif;font-weight:600;font-size:29px;color:var(--white)}
.welcome h2{font-family:'IBM Plex Sans',sans-serif;font-weight:600;font-size:37px;color:var(--white);letter-spacing:.5px;margin-top:4px}
.welcome .rule{width:60px;height:4px;background:var(--white);margin-top:16px}
.welcome p{margin-top:24px;font-size:13.5px;line-height:22.5px;color:#fbe6c7;width:405px}
.welcome .btn{position:relative;margin-top:22px;width:136px;height:40px;background:var(--green);font-size:13px}

/* blog */
.blog-band{left:0;top:1870px;width:1200px;height:625px;background:var(--gray)}
.blog-lead{left:3px;top:2033px;width:290px;height:385px;background:#f2f2f2;box-shadow:0 2px 12px rgba(0,0,0,.12);padding:40px 28px 0}
.date-tag{display:inline-block;background:var(--green);color:var(--white);font-size:13.5px;padding:7px 14px}
.blog-lead h3{margin-top:24px;font-family:'Roboto',sans-serif;font-weight:500;font-size:18px;line-height:23px;color:var(--ink)}
.blog-lead p{margin-top:14px;font-size:12.8px;line-height:19px;color:var(--text)}
.blog-lead a{display:block;margin-top:16px;font-size:13px;color:var(--green);text-decoration:underline}
.blog-card{top:2036px;width:284px;height:382px;background:var(--white);box-shadow:0 2px 8px rgba(0,0,0,.1)}
.blog-card .pic{width:284px;height:270px}
.blog-card h3{padding:18px 16px 0;font-weight:700;font-size:13.5px;line-height:22px;color:var(--ink)}
.blog-card .date{padding:6px 16px 0;font-size:13.5px;color:var(--green);display:flex;align-items:center;gap:6px;font-weight:500}

/* resources */
.resource{top:2683px;width:306px;height:395px;background:var(--white);box-shadow:0 2px 10px rgba(0,0,0,.14);text-align:center}
.resource .pic{height:195px}
.resource h3{margin-top:26px;font-weight:700;font-size:17px;color:var(--ink)}
.resource p{margin-top:14px;padding:0 24px;font-size:13.5px;line-height:22.5px;color:var(--text)}

/* testimonials */
.clients{left:0;top:3172px;width:1200px;height:560px;background:linear-gradient(120deg,#86c23c 0%,#74b22c 55%,#6aa326 100%)}
.clients .section-title{color:var(--white)}
.clients .title-rule{background:var(--white)}
.quote{top:3386px;width:456px;height:232px;background:var(--white);padding:66px 32px 0}
.quote .mark{position:absolute;right:30px;top:36px}
.quote h5{font-weight:500;font-size:13.5px;color:var(--ink)}
.quote p{margin-top:18px;font-size:12.5px;line-height:19.5px;color:var(--text)}
.avatar{width:72px;height:72px;border-radius:50%;background:linear-gradient(#c7c1ba,#8a8078);border:3px solid var(--white)}

/* newsletter */
.news-art{left:140px;top:3840px;width:440px;height:270px;border-radius:10px;background:linear-gradient(135deg,#f4f1ea 0%,#dfe6ef 50%,#f5f5f5 100%)}
.news-divider{left:615px;top:3860px;width:1px;height:235px;background:#e3e3e3}
.news h2{font-family:'IBM Plex Sans',sans-serif;font-weight:600;font-size:36px;color:var(--ink)}
.news p{margin-top:14px;font-size:13.5px;line-height:22px;color:var(--text);width:390px}
.email{left:662px;top:3970px;width:393px;height:46px;border:1px solid #d6d6d6;font-size:11px;color:var(--muted);padding:15px 18px;box-shadow:0 1px 4px rgba(0,0,0,.06)}
.subscribe{left:662px;top:4036px;width:393px;height:44px;background:var(--green);font-size:15px}

/* why */
.why{left:0;top:4200px;width:1200px;height:538px;background:linear-gradient(100deg,#7c94a7 0%,#a9bcca 55%,#d5dde3 100%)}
.why-art{left:560px;top:4220px;width:640px;height:518px;background:radial-gradient(ellipse at 45% 55%,rgba(87,136,52,.55) 0%,rgba(150,160,160,.25) 45%,rgba(255,255,255,0) 70%)}
.why-copy{left:143px;top:4340px}
.why-copy h2{font-family:'IBM Plex Sans',sans-serif;font-weight:600;font-size:31px;color:var(--white);letter-spacing:.5px}
.why-copy .rule{width:76px;height:3px;background:var(--white);margin-top:22px}
.why-copy p{margin-top:20px;font-size:14px;line-height:25.5px;color:#eef2f5;width:420px}
.why-copy .btn{position:relative;margin-top:26px;width:150px;height:41px;background:var(--orange);font-size:14px}

/* footer */
.footer{left:0;top:4738px;width:1200px;height:296px;background:var(--footer);font-family:'Poppins',sans-serif;color:#e6e6e6}
.contact{top:72px;display:flex;gap:18px;font-size:15px;line-height:22px;letter-spacing:.5px}
.v-rule{top:72px;width:1px;height:40px;background:#666}
.f-rule{left:210px;top:156px;width:836px;height:1px;background:#3a3a3a}
.f-links{left:210px;top:196px;font-size:14px}
.f-copy{left:210px;top:230px;font-size:14px}
.socials{left:793px;top:190px;display:flex;gap:16px}
.socials span{width:36px;height:36px;border-radius:50%;border:2px solid #ddd;display:block}
</style>
</head>
<body>

<!-- HERO -->
<div class="fill hero" role="img" aria-label="Woman in glasses writing in a notebook beside a laptop in a bright office"></div>
<div class="abs brand">
  <span class="brand-dot"></span>
  <span class="brand-name">Harvest Velmora</span>
</div>
<div class="abs call">
  <svg width="34" height="34" viewBox="0 0 34 34"><circle cx="17" cy="17" r="17" fill="#7cb82f"/><path d="M12 9l3 5-2 2c1 3 3 5 6 6l2-2 5 3-2 3c-7 0-14-7-14-14z" fill="#fff"/></svg>
  <span>Call Us: 1-808-5550-1942</span>
</div>
<div class="btn register">Register</div>
<nav class="abs nav">
  <span class="active">Home</span><span>About</span><span>Blog</span><span>Resource</span><span>Book Review</span><span>Contact Us</span>
</nav>
<div class="abs hero-box">
  <h1>Harvest Velmora… beside you. Helping your money grow branches.</h1>
</div>
<div class="btn hero-btn">Book Review</div>
<div class="abs dots"><span class="on"></span><span></span><span></span></div>

<!-- SERVICES -->
<h2 class="section-title" style="top:815px">OUR SERVICES</h2>
<div class="title-rule" style="top:880px"></div>

<div class="abs service" style="left:143px">
  <div class="service-icon"><svg width="60" height="60" viewBox="0 0 60 60" fill="none" stroke="#fff" stroke-width="3"><rect x="14" y="12" width="32" height="38" rx="3"/><path d="M21 24h18M21 32h18M21 40h10"/></svg></div>
  <h3>NEMO ENIM IPSAM</h3>
  <p>Lorem ipsum dolor sit amet, cetur adipiscing elit, sed do eiusmod tempor incididunt ut labore et dolore magna aliqua. Ut enim ad minim veniam, quis nostrud exation ullamco laboris nisi</p>
</div>
<div class="abs service" style="left:460px">
  <div class="service-icon"><svg width="60" height="60" viewBox="0 0 60 60" fill="none" stroke="#fff" stroke-width="3"><circle cx="28" cy="32" r="17"/><path d="M11 32h34M28 15c-8 10-8 24 0 34M28 15c8 10 8 24 0 34"/><path d="M38 20l10-10M42 10h6v6"/></svg></div>
  <h3>NEMO ENIM IPSAM</h3>
  <p>Lorem ipsum dolor sit amet, cetur adipiscing elit, sed do eiusmod tempor incididunt ut labore et dolore magna aliqua. Ut enim ad minim veniam, quis nostrud exation ullamco laboris nisi</p>
</div>
<div class="abs service" style="left:777px">
  <div class="service-icon"><svg width="60" height="60" viewBox="0 0 60 60" fill="none" stroke="#fff" stroke-width="3"><rect x="12" y="14" width="36" height="26" rx="2"/><path d="M18 34l8-8 6 5 10-11"/><path d="M22 48h16M30 40v8"/></svg></div>
  <h3>NEMO ENIM IPSAM</h3>
  <p>Lorem ipsum dolor sit amet, cetur adipiscing elit, sed do eiusmod tempor incididunt ut labore et dolore magna aliqua. Ut enim ad minim veniam, quis nostrud exation ullamco laboris nisi</p>
</div>

<!-- WELCOME -->
<div class="fill welcome-art" role="img" aria-label="Young green seedlings growing from stacks of gold coins in dark soil"></div>
<div class="abs welcome">
  <h4>Welcome to</h4>
  <h2>HARVEST VELMORA</h2>
  <div class="rule"></div>
  <p>Lorem ipsum dolor sit amet, consectetur adipiscing elit, sed do eiusmod tempor incididunt ut labore et dolore magna aliqua. Ut enim ad minim veniam, quis nostrud exercitation ullamco laboris nisi ut aliquip ex ea commodo consequat. Duis aute irure dolor in reprehenderit in voluptate velit esse cillum dolore eu fugiat nulla pariatur. Excepteur sint occaecat cupidatat non proident, sunt in culpa qui officia</p>
  <div class="btn">Learn More</div>
</div>

<!-- BLOG -->
<div class="fill blog-band"></div>
<h2 class="section-title" style="top:1928px;font-size:30px">LATEST BLOG</h2>
<div class="title-rule" style="top:1988px"></div>

<div class="abs blog-lead">
  <span class="date-tag">Feb 12, 2020</span>
  <h3>Nemo enim ipsam volupta Tem quia voluptas sit</h3>
  <p>Lorem ipsum dolor sit amet, consectetur adipiscing elit, sed do eiusmod tempor incididunt ut labore et dolore magna aliqua. Ut enim ad minim veniam, quis nostrud exercitation ullamco laboris nisi ut aliquip ex ea commodo consequat. Duis aute irure dolor</p>
  <a>Read More ›</a>
</div>

<div class="abs blog-card" style="left:312px">
  <div class="pic" role="img" aria-label="Woman in a polka-dot blouse working on a laptop" style="background:linear-gradient(160deg,#e4e4e2,#b9b6b1)"></div>
  <h3>NEMO ENIM IPSAM VOLUPTATEM QUIA VOLUPTAS SIT ASPNATUR</h3>
  <div class="date"><svg width="12" height="12" viewBox="0 0 12 12"><rect x="1" y="2" width="10" height="9" fill="none" stroke="#7cb82f" stroke-width="1.5"/><path d="M1 5h10" stroke="#7cb82f" stroke-width="1.5"/></svg>March 1st, 2020</div>
</div>
<div class="abs blog-card" style="left:608px">
  <div class="pic" role="img" aria-label="Smiling woman standing in an office" style="background:linear-gradient(160deg,#cfc8bd,#8c7f72)"></div>
  <h3>NEMO ENIM IPSAM VOLUPTATEM QUIA VOLUPTAS SIT ASPNATUR</h3>
  <div class="date"><svg width="12" height="12" viewBox="0 0 12 12"><rect x="1" y="2" width="10" height="9" fill="none" stroke="#7cb82f" stroke-width="1.5"/><path d="M1 5h10" stroke="#7cb82f" stroke-width="1.5"/></svg>March 1st, 2020</div>
</div>
<div class="abs blog-card" style="left:903px">
  <div class="pic" role="img" aria-label="Hand pointing at financial charts on a laptop screen" style="background:linear-gradient(160deg,#6d7584,#2f3440)"></div>
  <h3>NEMO ENIM IPSAM VOLUPTATEM QUIA VOLUPTAS SIT ASPNATUR</h3>
  <div class="date"><svg width="12" height="12" viewBox="0 0 12 12"><rect x="1" y="2" width="10" height="9" fill="none" stroke="#7cb82f" stroke-width="1.5"/><path d="M1 5h10" stroke="#7cb82f" stroke-width="1.5"/></svg>March 1st, 2020</div>
</div>

<!-- RESOURCE -->
<h2 class="section-title" style="top:2568px">RESOURCE</h2>
<div class="title-rule" style="top:2632px"></div>

<div class="abs resource" style="left:111px">
  <div class="pic" role="img" aria-label="Hands reviewing printed charts with a calculator" style="background:linear-gradient(150deg,#5a6470,#c9d2dc)"></div>
  <h3>NEMO ENIM IPSAM</h3>
  <p>Sed ut perspiciatis unde omnis iste natus error sit voluptatem accusantium doloremque laudantium, totam rem aperiam, eaque ipsa quae ab illo inntore veritatis et quasi architector</p>
</div>
<div class="abs resource" style="left:447px">
  <div class="pic" role="img" aria-label="Smiling adviser in glasses talking with a client" style="background:linear-gradient(150deg,#d4d2cc,#7d7a74)"></div>
  <h3>NEMO ENIM IPSAM</h3>
  <p>Sed ut perspiciatis unde omnis iste natus error sit voluptatem accusantium doloremque laudantium, totam rem aperiam, eaque ipsa quae ab illo inntore veritatis et quasi architector</p>
</div>
<div class="abs resource" style="left:783px">
  <div class="pic" role="img" aria-label="Person holding a tablet with market charts in front of a trading board" style="background:linear-gradient(150deg,#6b3a34,#1f2a3a)"></div>
  <h3>NEMO ENIM IPSAM</h3>
  <p>Sed ut perspiciatis unde omnis iste natus error sit voluptatem accusantium doloremque laudantium, totam rem aperiam, eaque ipsa quae ab illo inntore veritatis et quasi architector</p>
</div>

<!-- CLIENTS -->
<div class="fill clients" role="img" aria-label="Soft green background with a faint seedling growing from coins"></div>
<h2 class="section-title" style="top:3240px">OUR CLIENT SAY</h2>
<div class="title-rule" style="top:3312px"></div>

<div class="abs quote" style="left:131px">
  <svg class="mark" width="36" height="28" viewBox="0 0 36 28"><path d="M0 0h15v14l-6 14H3l5-14H0zM20 0h15v14l-6 14h-6l5-14h-8z" fill="#7cb82f"/></svg>
  <h5>Tessa - Harvest Velmora</h5>
  <p>Lorem ipsum dolor sit amet, consectetur adipiscing elit, sed do eiusmod tempor incididunt ut labore et dolore magna aliqua. Ut enim ad minim veniam, quis nostrud exercitation ullamco laboris nisi ut aliquip ex ea commodo consequat. Duis aute irure dolor in reprehenderit in voluptate velit esse cillum dolore</p>
</div>
<div class="abs avatar" style="left:163px;top:3320px" role="img" aria-label="Client portrait"></div>

<div class="abs quote" style="left:612px">
  <svg class="mark" width="36" height="28" viewBox="0 0 36 28"><path d="M0 0h15v14l-6 14H3l5-14H0zM20 0h15v14l-6 14h-6l5-14h-8z" fill="#7cb82f"/></svg>
  <h5>Tessa - Harvest Velmora</h5>
  <p>Lorem ipsum dolor sit amet, consectetur adipiscing elit, sed do eiusmod tempor incididunt ut labore et dolore magna aliqua. Ut enim ad minim veniam, quis nostrud exercitation ullamco laboris nisi ut aliquip ex ea commodo consequat. Duis aute irure dolor in reprehenderit in voluptate velit esse cillum dolore</p>
</div>
<div class="abs avatar" style="left:643px;top:3320px" role="img" aria-label="Client portrait"></div>

<!-- NEWSLETTER -->
<div class="fill news-art" role="img" aria-label="Illustration of a person relaxing on a cloud with a phone while envelopes fly around"></div>
<div class="news-divider abs"></div>
<div class="abs news" style="left:660px;top:3835px">
  <h2>Sign up for newsletter</h2>
  <p>Sed ut perspiciatis unde omnis iste natus error sit votem accusantium doloremque laudantium, totam</p>
</div>
<div class="abs email">Enter Email</div>
<div class="btn subscribe">Subscribe</div>

<!-- WHY -->
<div class="fill why"></div>
<div class="fill why-art" role="img" aria-label="Hand watering a potted plant shaped like a dollar sign"></div>
<div class="abs why-copy">
  <h2>WHY HARVEST VELMORA?</h2>
  <div class="rule"></div>
  <p>Lorem ipsum dolor sit amet, consectetur adipiscing elit, sed do eiusmod tempor incididunt ut labore et dolore magna aliqua. Ut enim ad minim veniam, quis nostrud exercitation ullamco laboris nisi ut aliquip ex ea commodo consequat. Duis aute irure dolor in reprehenderit in voluptate</p>
  <div class="btn">Learn More</div>
</div>

<!-- FOOTER -->
<footer class="fill footer">
  <div class="abs contact" style="left:208px">
    <svg width="16" height="22" viewBox="0 0 16 22" style="margin-top:4px"><path d="M8 1a7 7 0 0 0-7 7c0 5 7 13 7 13s7-8 7-13a7 7 0 0 0-7-7z" fill="none" stroke="#ddd" stroke-width="1.6"/><circle cx="8" cy="8" r="2.5" fill="none" stroke="#ddd" stroke-width="1.6"/></svg>
    <span>Harvest Velmora 71 Larchmere<br>Rd, Ostrell, 3184</span>
  </div>
  <div class="abs v-rule" style="left:522px"></div>
  <div class="abs contact" style="left:550px">
    <svg width="18" height="18" viewBox="0 0 18 18" style="margin-top:4px"><path d="M3 1l4 5-2 2c1 2 3 4 5 5l2-2 5 4-2 2C8 17 1 10 1 3z" fill="none" stroke="#ddd" stroke-width="1.5"/></svg>
    <span>Phone:<br>(808) 5550 7316</span>
  </div>
  <div class="abs v-rule" style="left:750px"></div>
  <div class="abs contact" style="left:780px">
    <svg width="20" height="14" viewBox="0 0 20 14" style="margin-top:6px"><rect x="1" y="1" width="18" height="12" fill="none" stroke="#ddd" stroke-width="1.5"/><path d="M1 1l9 7 9-7" fill="none" stroke="#ddd" stroke-width="1.5"/></svg>
    <span>E-mail:<br>hello@harvestvelmora.com</span>
  </div>
  <div class="abs f-rule"></div>
  <div class="abs f-links">Home &nbsp;|&nbsp; Affiliate &nbsp;|&nbsp; My podcast &nbsp;|&nbsp; Blog &nbsp;|&nbsp; Contact Us</div>
  <div class="abs f-copy">© 2020 Harvest Velmora. All Rights Reserved.</div>
  <div class="abs socials"><span></span><span></span><span></span><span></span></div>
</footer>

</body>
</html>
```